Business Card for my building company

I would like the card to make a statement, so as soon as you see the card you think "wow nice card' and then read the details on the card its self. Also i would like to be able to put in the detail for the MUST HAVES so please Crete a box that i can alter depending on who in my business needs the cards. Thank you

Target Market(s)

Any one looking to build a house/ townhouse or duplex

Industry/Entity Type

Home Builder

Contact Information for Business Card

I would like the card to have the logo on the card and the must haves

Font styles to use
Sans Serif

Requirements
Must have
• Name
• Phone Number
• Email Address
• Website
• Licence Number
• Abn

```html
<!DOCTYPE html>
<html lang="en">
<head>
<meta charset="utf-8">
<title>Ridgeline Homes – Business Card</title>
<link rel="stylesheet" href="https://fonts.googleapis.com/css2?family=Open+Sans:wght@400;600;700&display=swap">
<style>
  :root {
    --page-bg: #d9d3c9;
    --wall-dark: #3a2a1e;
    --wall-mid: #6b5240;
    --wall-light: #8a6d55;
    --panel-tint: rgba(120, 100, 85, 0.35);
    --band-dark: #2a1c14;
    --gold: #b8923f;
    --gold-light: #d9b766;
    --gold-deep: #8a6a2a;
    --text-light: #ece6dc;
    --text-soft: #d6cdbf;
  }
  * { margin: 0; padding: 0; box-sizing: border-box; }
  html, body {
    width: 1200px; height: 970px; overflow: hidden;
    background: var(--page-bg);
    font-family: "Open Sans", Arial, sans-serif;
  }
  .card {
    position: absolute; left: 50px; top: 156px;
    width: 1100px; height: 658px;
    overflow: hidden;
    box-shadow: 0 10px 30px rgba(0,0,0,0.25);
  }
  .wall {
    position: absolute; inset: 0 0 133px 0;
    background:
      radial-gradient(ellipse at 45% 40%, var(--wall-light) 0%, var(--wall-mid) 45%, var(--wall-dark) 100%);
  }
  .detail-panel {
    position: absolute; left: 619px; top: 0; right: 0; height: 507px;
    background: var(--panel-tint);
  }
  .brand {
    position: absolute; left: 56px; top: 93px; width: 427px; height: 391px;
    display: flex; flex-direction: column; align-items: center; justify-content: center; gap: 26px;
  }
  .brand-mark {
    width: 110px; height: 110px; background: var(--gold);
  }
  .brand-name {
    color: var(--gold-light); font-weight: 700; font-size: 56px;
    line-height: 1.05; text-align: center; letter-spacing: 1px;
  }
  .details {
    position: absolute; right: 89px; top: 0; text-align: right;
    color: var(--text-light);
  }
  .person-name {
    position: absolute; right: 0; top: 80px; white-space: nowrap;
    font-size: 46px; font-weight: 400; color: var(--text-light);
  }
  .registration {
    position: absolute; right: 0; top: 200px; white-space: nowrap;
    font-size: 31px; line-height: 49px; color: var(--text-soft);
  }
  .contacts {
    position: absolute; right: 0; top: 350px; list-style: none;
  }
  .contacts li {
    display: flex; align-items: center; justify-content: flex-end; gap: 14px;
    height: 45px; white-space: nowrap;
    font-size: 29px; color: var(--text-soft);
  }
  .contact-icon {
    width: 29px; height: 29px; background: var(--gold);
    display: flex; align-items: center; justify-content: center; flex: none;
  }
  .band-dark {
    position: absolute; left: 0; right: 0; top: 507px; height: 44px;
    background: linear-gradient(to bottom, var(--band-dark), #1b120d);
  }
  .line-gold {
    position: absolute; left: 0; right: 0; top: 556px; height: 6px; background: var(--gold);
  }
  .line-dark {
    position: absolute; left: 0; right: 0; top: 566px; height: 6px; background: var(--band-dark);
  }
  .band-gold {
    position: absolute; left: 0; right: 0; top: 578px; bottom: 0;
    background: linear-gradient(to right, var(--gold-deep), var(--gold) 40%, var(--gold-light) 75%, var(--gold));
  }
</style>
</head>
<body>
  <div class="card">
    <div class="wall" role="img" aria-label="Stone brick wall texture in warm brown tones"></div>
    <div class="detail-panel"></div>

    <div class="brand">
      <div class="brand-mark"></div>
      <div class="brand-name">Ridgeline<br>Homes</div>
    </div>

    <div class="details" style="width:600px;height:507px;">
      <div class="person-name">Daniel Harlow</div>
      <div class="registration">
        Lic No.4821930<br>
        ABN: 31704928615
      </div>
      <ul class="contacts">
        <li>0400 318 642
          <span class="contact-icon">
            <svg width="18" height="18" viewBox="0 0 24 24"><path d="M6.6 10.8a15 15 0 0 0 6.6 6.6l2.2-2.2a1 1 0 0 1 1-.25 11.4 11.4 0 0 0 3.6.57 1 1 0 0 1 1 1V20a1 1 0 0 1-1 1A17 17 0 0 1 3 4a1 1 0 0 1 1-1h3.5a1 1 0 0 1 1 1c0 1.25.2 2.45.57 3.57a1 1 0 0 1-.25 1z" fill="#3a2a1e"/></svg>
          </span>
        </li>
        <li>info@ridgeline.com
          <span class="contact-icon">
            <svg width="18" height="14" viewBox="0 0 24 18"><rect x="1" y="1" width="22" height="16" fill="none" stroke="#3a2a1e" stroke-width="2"/><path d="M1 1l11 9 11-9" fill="none" stroke="#3a2a1e" stroke-width="2"/></svg>
          </span>
        </li>
        <li>www.ridgeline-homes.com
          <span class="contact-icon">
            <svg width="18" height="18" viewBox="0 0 24 24"><circle cx="12" cy="12" r="10" fill="none" stroke="#3a2a1e" stroke-width="2"/><ellipse cx="12" cy="12" rx="4.5" ry="10" fill="none" stroke="#3a2a1e" stroke-width="2"/><path d="M2 12h20" stroke="#3a2a1e" stroke-width="2"/></svg>
          </span>
        </li>
      </ul>
    </div>

    <div class="band-dark"></div>
    <div class="line-gold"></div>
    <div class="line-dark"></div>
    <div class="band-gold"></div>
  </div>
</body>
</html>
```